Quelvon Corporate General Presentation

Quelvon is a leading player in ICT (Information Communication Technology) cooling, we need a design for our corporate general presentation.

Attached is a reference of content

Our logo main color is industrial blue, our technology is green (energy saving).

existing website: www.quel-von.com www.quel-von.uk

Target Market(s)

Global

Industry/Entity Type

Communication

Number of Pages Required

5+ page

Font styles to use
Serif
Sans Serif

Colors
0255a3
3176b5
0293ce
33a6d7
9bcb3c

```html
<!DOCTYPE html>
<html lang="en">
<head>
<meta charset="utf-8">
<title>Data Center Solutions</title>
<link href="https://fonts.googleapis.com/css2?family=Lato:wght@300;400&display=swap" rel="stylesheet">
<style>
  :root {
    --bg: #ffffff;
    --title: #8d939b;
    --body-text: #8a8f96;
    --blue-strong: #33b8f0;
    --blue-mid: #a9dcf6;
    --blue-light: #d6effc;
    --blue-ink: #2a9fd6;
    --white: #ffffff;
  }
  * { margin: 0; padding: 0; box-sizing: border-box; }
  html, body { width: 1200px; height: 675px; overflow: hidden; background: var(--bg); }
  .slide {
    position: relative; width: 1200px; height: 675px;
    font-family: "Lato", sans-serif; color: var(--body-text);
  }
  .slide-title {
    position: absolute; top: 44px; left: 0; width: 100%;
    text-align: center; font-weight: 400; font-size: 31px; color: var(--title);
  }
  .slide-subtitle {
    position: absolute; top: 85px; left: 0; width: 100%;
    text-align: center; font-weight: 400; font-size: 17px; color: var(--title);
  }
  .circles { position: absolute; left: 0; top: 0; }
  .solution {
    position: absolute; text-align: center; color: var(--white);
    font-size: 17px; line-height: 21px;
  }
  .solution-name { text-transform: uppercase; }
  .solution--datacentre { left: 195px; top: 267px; width: 262px; }
  .solution--telecom { left: 490px; top: 267px; width: 220px; }
  .solution--medical { left: 765px; top: 267px; width: 220px; color: var(--blue-ink); }
  .company-note {
    position: absolute; top: 513px; left: 140px; width: 920px;
    text-align: center; font-size: 16px; line-height: 30px; color: var(--body-text);
  }
</style>
</head>
<body>
<main class="slide">
  <h1 class="slide-title">Data Center Solutions</h1>
  <p class="slide-subtitle">Our solutions are recognized as reliable, precise and energy efficient.</p>

  <svg class="circles" width="1200" height="675" viewBox="0 0 1200 675" aria-hidden="true">
    <circle cx="875" cy="333" r="150" fill="var(--blue-light)"/>
    <circle cx="600" cy="333" r="150" fill="var(--blue-mid)" opacity="0.92"/>
    <circle cx="325" cy="333" r="150" fill="var(--blue-strong)"/>
    <g class="icon-pin" fill="none" stroke="#fff" stroke-width="2.4" stroke-linejoin="round">
      <path d="M325 245c-9-11-16-20-16-29a16 16 0 0 1 32 0c0 9-7 18-16 29z"/>
      <circle cx="325" cy="216" r="6"/>
    </g>
    <g class="icon-trophy" fill="none" stroke="#fff" stroke-width="2.4" stroke-linejoin="round" stroke-linecap="round">
      <path d="M589 203h22v10a11 11 0 0 1-22 0z"/>
      <path d="M589 207h-7a6 6 0 0 0 9 11"/>
      <path d="M611 207h7a6 6 0 0 1-9 11"/>
      <path d="M600 224v9M592 237h16v5h-16z"/>
    </g>
    <g class="icon-flame" fill="none" stroke="var(--blue-ink)" stroke-width="2.4" stroke-linejoin="round">
      <path d="M875 243c-10 0-16-7-16-15 0-10 8-14 8-22 6 4 8 9 8 13 2-3 4-6 4-11 7 5 12 13 12 20 0 8-6 15-16 15z"/>
      <path d="M875 243c-4 0-7-3-7-7 0-4 4-7 5-11 4 3 9 6 9 11 0 4-3 7-7 7z"/>
    </g>
  </svg>

  <section class="solution solution--datacentre">
    <p class="solution-name">Data Centre Cooling</p>
    <p>Wide portfolio of Computer<br>Room Air Conditioners, In<br>Row, In Rack and Adiabatic<br>Cooling Solutions.</p>
  </section>
  <section class="solution solution--telecom">
    <p class="solution-name">Telecom Cooling</p>
    <p>Energy Saving &amp; Cost<br>Effective, Fresh Air,<br>Direct Expansion &amp;<br>Adiabatic Cooling<br>Solutions for Cabinets,<br>Shelters, Exchanges &amp;<br>Base Stations.</p>
  </section>
  <section class="solution solution--medical">
    <p class="solution-name">Medical Equipment<br>Cooling</p>
    <p>State-of-the-Art<br>Medical Chillers, Heat<br>Exchanges and Air<br>Conditioners.</p>
  </section>

  <p class="company-note">QUELVON’ products are sold all over the world, and it is now one of the world famous cooling and air-conditioning product<br>supplier, as well as the internationally competitive professional supplier of cooling and air-conditioning equipment and<br>engineering.</p>
</main>
</body>
</html>
```